Brackenfold Health Web Page

We need a visually exciting webpage that introduces people to our practice. We are a practice that has both physiotherapy and psychology and we need the page to reflect this. We are also split across two practice locations. We need the page to be able to be updated regularly to include a blog spot and the linking in of our facebook page. There should be tabs to introduce our practitioners with some blurbs about them, a tab for people to be able to contact us, a tab to read about physiotherapy services and a tab to talk about psychology services. If there are other tabs than please include these. We are a practice that has treated world class athlete on a regular basis and see our selves as leaders in the field and the website must reflect this. I do not want basic clip-arty type things that anyone could have, we have to have something that draws people in.
Firstly, thanks everyone for their designs. I have attached some links to some physiotherapy websites that I think contain some interesting information and/or layout, as well as some comments,
Hi all,
Reason: Hi Guys,
We are so very close to finding a great design. I feel that we just need a bit of extra time to be able to clinch where we want to be. Thanks for your fantastic designs :)
Regards,
Oliver and Ruth
- 2 Practice Addresses (details to follow for right applications)
Psychology aspect
Physiotherapy aspect
Ability to update blog

```html
<!DOCTYPE html>
<html lang="en">
<head>
<meta charset="utf-8">
<title>Brackenfold Health</title>
<link href="https://fonts.googleapis.com/css2?family=Exo:wght@400;500;600&family=Open+Sans:ital,wght@0,400;0,600;1,400&display=swap" rel="stylesheet">
<style>
:root{
  --blue:#1497cf;
  --blue-dark:#0f7fb0;
  --purple:#7320c8;
  --purple-line:#8d45d6;
  --grey-bg:#ebebeb;
  --ink:#1c1c1c;
  --body:#555;
  --red:#c0392b;
  --white:#fff;
}
*{box-sizing:border-box;margin:0;padding:0}
html,body{width:738px;height:1200px;overflow:hidden;background:var(--white)}
body{font-family:"Open Sans",Arial,sans-serif;color:var(--ink)}
.page{width:738px;height:1200px;position:relative}
.wrap{padding:0 77px}

/* header */
.site-header{height:61px;background:var(--blue);position:relative;color:var(--white)}
.brand{position:absolute;left:77px;top:13px;font-family:"Exo",sans-serif;font-weight:600;font-size:17px;line-height:16px;letter-spacing:.5px;text-transform:uppercase}
.call{position:absolute;right:68px;top:13px;font-size:10px;font-style:italic}
.main-nav{position:absolute;right:68px;top:32px;display:flex;gap:8px;font-family:"Exo",sans-serif;font-size:10px;font-weight:500;text-transform:uppercase}
.main-nav a{color:var(--white);text-decoration:none}
.main-nav .sep{opacity:.85}
.main-nav .current{border-bottom:1px solid var(--white);padding-bottom:3px}

/* hero */
.hero{height:309px;position:relative;background:linear-gradient(100deg,#d9d9d6 0%,#c9c8c3 35%,#a8a69f 60%,#e2e0da 85%,#cfcdc7 100%)}
.hero-panel{position:absolute;left:78px;top:41px;width:322px;height:130px;background:rgba(255,255,255,.45)}
.hero h1{position:absolute;left:100px;top:66px;font-family:"Exo",sans-serif;font-weight:500;font-size:20px;line-height:20px;text-transform:uppercase;color:var(--ink)}
.hero p{position:absolute;left:97px;top:110px;width:290px;font-size:10px;line-height:12px;color:#222}
.btn{display:inline-block;background:var(--blue);color:var(--white);font-size:7.5px;text-decoration:none}
.hero .btn{position:absolute;left:99px;top:142px;width:100px;height:20px;line-height:20px;text-align:center}
.slider-ctrl{position:absolute;right:56px;bottom:22px;display:flex;align-items:center;gap:4px}

/* welcome */
.welcome{height:98px;background:var(--grey-bg);text-align:center;padding-top:26px}
.rule-title{display:flex;align-items:center;justify-content:center;gap:8px;font-family:"Exo",sans-serif;font-weight:500;font-size:14px}
.rule-title::before,.rule-title::after{content:"";width:115px;height:1px;background:#c7c7c7;border-right:7px solid #c7c7c7;border-left:none}
.rule-title::after{border-right:none;border-left:7px solid #c7c7c7}
.welcome p{width:410px;margin:6px auto 0;font-size:7px;line-height:9.5px;color:#333}

/* practitioners */
.practitioners{height:179px;background:var(--purple);color:var(--white);padding-top:26px}
.section-head{display:flex;justify-content:space-between;align-items:center;padding-bottom:10px;border-bottom:1px solid var(--purple-line)}
.section-head h2{font-family:"Exo",sans-serif;font-weight:500;font-size:14px}
.btn-light{background:var(--white);color:var(--purple);width:96px;height:15px;line-height:15px;text-align:center;font-size:7px}
.cards{display:flex;justify-content:space-between;margin-top:13px}
.card{width:276px;display:flex;gap:6px}
.thumb{flex:none;width:108px;height:70px;background:linear-gradient(135deg,#8a98a8,#c48b76 55%,#7a2a2e)}
.card h3{font-family:"Open Sans",sans-serif;font-weight:400;font-size:11px;line-height:13px}
.card p{font-size:6.6px;line-height:9px;margin-top:3px}
.meta{font-size:6px;font-style:italic;margin-top:5px;display:flex;gap:8px}

/* blog */
.blog{height:299px;background:var(--grey-bg);padding-top:32px}
.blog .section-head{border-bottom:2px solid #d3d3d3;padding-bottom:6px}
.blog .section-head h2{color:var(--ink)}
.btn-blue{width:74px;height:15px;line-height:15px;text-align:center}
.blog-grid{display:grid;grid-template-columns:276px 276px;justify-content:space-between;row-gap:20px;margin-top:11px}
.post{display:flex;gap:6px}
.post-thumb{flex:none;width:108px;height:84px;position:relative;background:linear-gradient(135deg,#6f8aa6,#b99a85 50%,#8a2b2e)}
.post-date{position:absolute;left:0;right:0;bottom:0;height:14px;background:#4a4a4a;color:var(--white);font-size:6px;font-style:italic;text-align:center;line-height:14px}
.post h3{font-weight:400;font-size:11px;line-height:13px}
.post p{font-size:6.6px;line-height:9px;color:#777;margin-top:4px}
.post-foot{margin-top:6px;padding-top:5px;border-top:1px solid #d3d3d3;display:flex;gap:10px;font-size:6.5px;align-items:center}
.learn{color:var(--red)}
.like{border:1px solid #bbb;background:#fff;padding:0 4px;color:#3b5998;font-size:6px}
.count{border:1px solid #bbb;background:#fff;padding:0 3px;color:#777;font-size:6px}

/* locations */
.locations{height:204px;position:relative;background:linear-gradient(90deg,#f1efe6 0%,#eeeada 60%,#e4e8dc 78%,#a9c6f2 86%,#9fc1f3 100%)}
.service-card{position:absolute;left:241px;top:42px;width:225px;height:93px;background:var(--white);border:1px solid #ccc;padding:4px;display:flex;gap:3px}
.service{flex:1;text-align:center;font-size:7px}
.service .img{height:72px;margin-bottom:3px}
.img-physio{background:linear-gradient(135deg,#d8cfc4,#8fa3b8)}
.img-psych{background:linear-gradient(135deg,#5a5f5c,#9aa39c)}
.pin-label{position:absolute;left:494px;top:72px;font-size:6px;font-weight:600;color:#a01a2a;line-height:7px}
.pin{position:absolute;left:476px;top:51px}

/* footer */
.site-footer{height:50px;background:var(--blue);color:var(--white);display:flex;align-items:center;padding:0 68px 0 94px;font-size:7px}
.social{display:flex;gap:3px;margin-right:14px}
.footer-nav{display:flex;gap:6px}
.copy{margin-left:auto}
</style>
</head>
<body>
<div class="page">
  <header class="site-header">
    <div class="brand">Brackenfold<br>Health</div>
    <div class="call">Call us at : 1800 555 019</div>
    <nav class="main-nav">
      <a href="#">Home</a><span class="sep">/</span>
      <a href="#" class="current">About Us</a><span class="sep">/</span>
      <a href="#">Practitioners</a><span class="sep">/</span>
      <a href="#">Our Services</a><span class="sep">/</span>
      <a href="#">Contact Us</a>
    </nav>
  </header>

  <section class="hero" role="img" aria-label="Physiotherapist stretching a patient's arm on a treatment table">
    <div class="hero-panel"></div>
    <h1>Brackenfold Health<br>Psychology Services</h1>
    <p>Lorem ipsum dolor sit amet, consectetur adipiscing elit. In fermentum dolor non augue pretium egestas.</p>
    <a class="btn" href="#">Make an Appointment</a>
    <div class="slider-ctrl">
      <svg width="12" height="14" viewBox="0 0 12 14"><path d="M9 1 3 7l6 6" stroke="#fff" stroke-width="2.5" fill="none"/></svg>
      <svg width="24" height="6"><rect width="6" height="6" fill="#fff"/><rect x="9" width="6" height="6" fill="#fff"/><rect x="18" width="6" height="6" fill="#fff"/></svg>
      <svg width="12" height="14" viewBox="0 0 12 14"><path d="m3 1 6 6-6 6" stroke="#fff" stroke-width="2.5" fill="none"/></svg>
    </div>
  </section>

  <section class="welcome">
    <h2 class="rule-title">Welcome to Brackenfold Health</h2>
    <p>Lorem ipsum dolor sit amet, consectetur adipiscing elit. In amet fermentum dolor non augue pretium egestas. Donec sem eros, at congue ut suere sit amet est. scelerisque viverra odio sit amet laoreet. Nec neque non justo rutrum tempor Lorem ipsum dolor sit amet, consectetur adipiscing elit.</p>
  </section>

  <section class="practitioners">
    <div class="wrap">
      <div class="section-head">
        <h2>Our Practitioners</h2>
        <a class="btn btn-light" href="#">Make an Appointment</a>
      </div>
      <div class="cards">
        <article class="card">
          <div class="thumb" role="img" aria-label="Practitioner with a clipboard in the gym"></div>
          <div>
            <h3>Lorem ipsum dolor amet ipsum dolor amet ipsum</h3>
            <p>Lorem ipsum dolor sit amet, consectetur adipiscing elit. In amet fermentum dolor non augue pretium egestas Lorem ipsum dolor sit amet, consectetur adipiscing elit. In amet fermentum dolor non augue pretium egestas.</p>
            <div class="meta"><span>&#9679; Posted by Marla</span><span>&#9675; 2 hour ago by</span></div>
          </div>
        </article>
        <article class="card">
          <div class="thumb" role="img" aria-label="Therapist guiding a patient lifting dumbbells"></div>
          <div>
            <h3>Lorem ipsum dolor amet ipsum dolor amet ipsum</h3>
            <p>Lorem ipsum dolor sit amet, consectetur adipiscing elit. In amet fermentum dolor non augue pretium egestas Lorem ipsum dolor sit amet, consectetur adipiscing elit. In amet fermentum dolor non augue pretium egestas.</p>
            <div class="meta"><span>&#9679; Posted by Marla</span><span>&#9675; 2 hour ago by</span></div>
          </div>
        </article>
      </div>
    </div>
  </section>

  <section class="blog">
    <div class="wrap">
      <div class="section-head">
        <h2>Blog Spot</h2>
        <a class="btn btn-blue" href="#">View All Blogs</a>
      </div>
      <div class="blog-grid">
        <article class="post">
          <div class="post-thumb" role="img" aria-label="Therapist guiding a patient lifting dumbbells"><span class="post-date">JANUARY 18, 2014</span></div>
          <div><h3>Lorem ipsum dolor amet ipsum dolor amet ipsum</h3><p>Lorem ipsum dolor sit amet, consectetur adipiscing elit. In amet fermentum dolor non augue pretium egestas.</p><div class="post-foot"><span class="learn">Learn More +</span><span class="like">Like</span><span class="count">61</span></div></div>
        </article>
        <article class="post">
          <div class="post-thumb" role="img" aria-label="Therapist guiding a patient lifting dumbbells"><span class="post-date">JANUARY 18, 2014</span></div>
          <div><h3>Lorem ipsum dolor amet ipsum dolor amet ipsum</h3><p>Lorem ipsum dolor sit amet, consectetur adipiscing elit. In amet fermentum dolor non augue pretium egestas.</p><div class="post-foot"><span class="learn">Learn More +</span><span class="like">Like</span><span class="count">61</span></div></div>
        </article>
        <article class="post">
          <div class="post-thumb" role="img" aria-label="Therapist guiding a patient lifting dumbbells"><span class="post-date">JANUARY 18, 2014</span></div>
          <div><h3>Lorem ipsum dolor amet ipsum dolor amet ipsum</h3><p>Lorem ipsum dolor sit amet, consectetur adipiscing elit. In amet fermentum dolor non augue pretium egestas.</p><div class="post-foot"><span class="learn">Learn More +</span><span class="like">Like</span><span class="count">61</span></div></div>
        </article>
        <article class="post">
          <div class="post-thumb" role="img" aria-label="Therapist guiding a patient lifting dumbbells"><span class="post-date">JANUARY 18, 2014</span></div>
          <div><h3>Lorem ipsum dolor amet ipsum dolor amet ipsum</h3><p>Lorem ipsum dolor sit amet, consectetur adipiscing elit. In amet fermentum dolor non augue pretium egestas.</p><div class="post-foot"><span class="learn">Learn More +</span><span class="like">Like</span><span class="count">61</span></div></div>
        </article>
      </div>
    </div>
  </section>

  <section class="locations" role="img" aria-label="Regional road map showing the practice location near the coast">
    <div class="service-card">
      <div class="service"><div class="img img-physio" role="img" aria-label="Physiotherapist with a patient"></div>Physiotherapy</div>
      <div class="service"><div class="img img-psych" role="img" aria-label="Psychology consultation"></div>Psychology</div>
    </div>
    <svg class="pin" width="18" height="26" viewBox="0 0 18 26"><path d="M9 1C4.6 1 1 4.5 1 8.9 1 15 9 25 9 25s8-10 8-16.1C17 4.5 13.4 1 9 1z" fill="#fff" stroke="#1497cf" stroke-width="1.5"/><circle cx="9" cy="9" r="4" fill="#1497cf"/></svg>
    <div class="pin-label">Brackenfold Health<br>Centre - Physiotherapy<br>&amp; Psychology</div>
  </section>

  <footer class="site-footer">
    <div class="social">
      <svg width="16" height="16"><rect x="3" y="3" width="10" height="10" fill="#fff" transform="rotate(45 8 8)"/></svg>
      <svg width="16" height="16"><rect x="3" y="3" width="10" height="10" fill="#fff" transform="rotate(45 8 8)"/></svg>
    </div>
    <nav class="footer-nav"><span>Home</span>/<span>About us</span>/<span>Practitioners</span>/<span>Our Services</span>/<span>Contact us</span></nav>
    <div class="copy">© 2014 Terms and Policy</div>
  </footer>
</div>
</body>
</html>
```